Business card for new business - financial management

I need a business card designed for my new business. I'm the owner / sole trader of QVB Consulting, which provides financial management services for Government. I'd like the design to incorporate the attached business name and colours. The design should include colour and not be too way out - it needs to look at home in a government environment.
Details to be included on the card are:
QVB Consulting
Miriam Haskett
0400 386 924
miriamrhaskett@fernmail.example
47 Pallister Crescent, Curtin ACT 2605
Single or double sided designs would be good.
Employees at Australian Federal Government agencies
Government

```html
<!DOCTYPE html>
<html lang="en">
<head>
<meta charset="utf-8">
<title>QVB Consulting – Business Card</title>
<link rel="stylesheet" href="https://fonts.googleapis.com/css2?family=Lato:wght@300;400;700;900&display=swap">
<style>
  :root {
    --stage: #e9e7e3;
    --card-white: #fbfbfb;
    --card-black: #0b0b0c;
    --teal-deep: #2c6f80;
    --teal-deep-end: #8fb2ba;
    --teal-mid: #3fa6b8;
    --teal-mid-end: #78cdd6;
    --teal-pale: #a4d9e1;
    --teal-pale-end: #d3eef1;
    --brand-teal: #3e8ea3;
    --brand-teal-dark: #5ea4bd;
    --icon-teal: #6fb6c4;
    --ink: #2e3436;
    --on-dark: #ffffff;
  }
  * { box-sizing: border-box; margin: 0; padding: 0; }
  html, body {
    width: 1200px;
    height: 1023px;
    overflow: hidden;
    background: var(--stage);
    font-family: "Lato", Arial, sans-serif;
  }
  .stage { position: relative; width: 1200px; height: 1023px; }

  .card {
    position: absolute;
    width: 640px;
    height: 366px;
    border-radius: 26px;
    overflow: hidden;
    box-shadow: 0 10px 28px rgba(0,0,0,.18);
  }

  /* Front */
  .card--front { left: 70px; top: 80px; background: var(--card-white); }
  .brand {
    position: absolute;
    color: var(--brand-teal);
    font-weight: 400;
    white-space: nowrap;
  }
  .card--front .brand { right: 56px; top: 88px; font-size: 42px; letter-spacing: .5px; }

  .tab {
    position: absolute;
    left: 0;
    height: 52px;
    border-radius: 0 26px 26px 0;
    padding-left: 40px;
    display: flex;
    flex-direction: column;
    justify-content: center;
  }
  .tab--name    { top: 180px; width: 340px; background: linear-gradient(90deg, var(--teal-deep), var(--teal-deep-end)); color: var(--on-dark); }
  .tab--address { top: 242px; width: 370px; background: linear-gradient(90deg, var(--teal-mid), var(--teal-mid-end)); color: var(--ink); }
  .tab--contact { top: 304px; width: 400px; background: linear-gradient(90deg, var(--teal-pale), var(--teal-pale-end)); color: var(--ink); }

  .person-name { font-weight: 900; font-size: 21px; line-height: 1.05; }
  .person-role { font-weight: 300; font-size: 14px; line-height: 1.2; }
  .address-line { font-weight: 400; font-size: 14.5px; line-height: 1.25; }
  .contact-line { display: flex; align-items: center; gap: 7px; font-size: 14px; line-height: 1.3; }
  .contact-icon { width: 12px; height: 12px; flex: none; }

  /* Back */
  .card--back {
    left: 490px; top: 577px;
    background: radial-gradient(ellipse at 35% 30%, #2a2c2e 0%, var(--card-black) 60%);
  }
  .card--back .brand {
    color: var(--brand-teal-dark);
    left: 50%; top: 50%;
    transform: translate(-50%, -50%);
    text-align: center;
    line-height: 1;
  }
  .brand-initials { display: block; font-size: 104px; letter-spacing: 4px; }
  .brand-word { display: block; font-size: 50px; margin-top: 6px; }
</style>
</head>
<body>
<main class="stage">
  <section class="card card--front" aria-label="Business card front">
    <div class="brand">QVB Consulting</div>

    <div class="tab tab--name">
      <span class="person-name">Miriam Haskett</span>
      <span class="person-role">owner</span>
    </div>

    <div class="tab tab--address">
      <span class="address-line">47 Pallister Crescent</span>
      <span class="address-line">Brindlewood ACT 2699</span>
    </div>

    <div class="tab tab--contact">
      <span class="contact-line">
        <svg class="contact-icon" viewBox="0 0 12 12" aria-hidden="true">
          <rect width="12" height="12" rx="2" fill="var(--icon-teal)"/>
          <path d="M3.4 2.6c.4-.3.9-.2 1.1.2l.6 1.1c.2.4.1.8-.2 1l-.4.3c.4.9 1 1.5 1.9 1.9l.3-.4c.2-.3.6-.4 1-.2l1.1.6c.4.2.5.7.2 1.1l-.5.6c-.4.4-1 .5-1.6.3C5 8.4 3.6 7 2.9 5.1c-.2-.6-.1-1.2.3-1.6z" fill="#fff"/>
        </svg>
        0400 386 924
      </span>
      <span class="contact-line">
        <svg class="contact-icon" viewBox="0 0 12 12" aria-hidden="true">
          <rect width="12" height="12" rx="2" fill="var(--icon-teal)"/>
          <rect x="2.2" y="3.4" width="7.6" height="5.2" rx=".6" fill="#fff"/>
          <path d="M2.4 3.7 6 6.4l3.6-2.7" fill="none" stroke="var(--icon-teal)" stroke-width=".8"/>
        </svg>
        miriamrhaskett@fernmail.example
      </span>
    </div>
  </section>

  <section class="card card--back" aria-label="Business card back">
    <div class="brand">
      <span class="brand-initials">QVB</span>
      <span class="brand-word">Consulting</span>
    </div>
  </section>
</main>
</body>
</html>
```